Neuartiges Verpackungsdesign für Erdnüsse mit Karamell in Puzzleform
Zielgruppe
Wir gründen eine Produktion für Lebensmittel. Es handelt sich hierbei um Erdnüsse mit Karamell. Unsere Zielgruppe ist von jung bis alt, beider Geschlechter.
Aufgabenstellung
Bei dem Produkt handelt es sich um eine Weiterentwicklung eines Klassikers. Es werden Nüsse mit Karamell überzogen und zu verschiedenen Formen verarbeitet, die Besonderheit liegt darin das durch ein neues technisches Verfahren ein höher Nussanteil erreicht wird und das Produkt zudem optisch schöner und geschmacklich leichter und knuspriger wirkt als bei der Konkurrenz.
Zudem wird Erdnussöl sowie verschiedene hochwertige Zusatzstoffe hinzugegeben, somit erhält das Produkt mehr ungesättigte Fettsäuren und ist zudem nicht nur ein gesunder sondern auch ein besonders schmackhafter Snack. Außerdem ist noch zu erwähnen das, dass Produkt vegan ist und glutenfrei. Zudem soll es als proteinreich deklariert werden, da mehr Erdnüsse und weniger Zucker dosiert werden.
Die größte Besonderheit ist jedoch das, dass Produkt in jeglicher Form gebracht werden kann. Es sind somit nicht nur quadratische oder Riegelartige Formen möglich. Die Formen reichen von Kreisen, Dreiecken bis zu Weihnachtsmänner und Osterhasen, aufgrund der Vielzahl der Formen welche möglich sind wird das Produkt “Tobble Crunchies“ genannt. Die Hauptform welche angestrebt wird, ist eine Puzzleform. Also es ist ein Snack welcher eine Puzzle Form besitzt.
Die Verpackung soll einen Klotzbodenbeutel darstellen, also eine Verpackung welche beispielsweise den Tam Tel‘s ähnelt. Die Maße der Verpackung sind 85mm in Breite, 160mm in Höhe und 65mm in Tiefe.
Das ganze Design sollte sehr modern sein und edel wirken, wie es beispielsweise bei hochwertigen Schokoladen wie bei Morwe der Fall ist, da in unseren Produkt hochwertiges Erdnussöl zum Einsatz kommt.
Zudem soll das Design nicht nur die mittlere bis ältere Generation ansprechen, sondern auch die Jugend mit dem Ziel sich gesünder zu ernähren und es sollen sogar Kinder angesprochen werden, da sehr viele Formen möglich sind und Kinder damit Puzzlen oder spielen könnten, so ähnlich wie es bei Wippfrucht von Wb..

```html
<!DOCTYPE html>
<html lang="de">
<head>
<meta charset="utf-8">
<title>Erdnuss-Karamell Bites – Verpackung Vorderseite</title>
<link href="https://fonts.googleapis.com/css2?family=Fjalla+One&family=Fira+Sans:wght@400&display=swap" rel="stylesheet">
<style>
  :root {
    --stage: #221e1a;
    --seal: #b8560c;
    --seal-dark: #a94c08;
    --bag: #eeb27c;
    --bag-light: #f6d2ab;
    --ink: #3a140c;
    --label: #ececec;
    --band: rgba(255, 236, 214, 0.7);
    --splash-a: #c7762c;
    --splash-b: #f0cf8a;
  }
  * { margin: 0; padding: 0; box-sizing: border-box; }
  html, body {
    width: 1091px; height: 1200px; overflow: hidden;
    background: var(--stage);
  }
  .pack {
    position: absolute; left: 285px; top: 45px;
    width: 520px; height: 1110px;
    background: linear-gradient(180deg, var(--bag) 0%, var(--bag) 55%, #f2c08f 100%);
    overflow: hidden;
    font-family: "Fira Sans", sans-serif;
    color: var(--ink);
  }
  .pack__seal {
    position: absolute; left: 0; top: 0; width: 100%; height: 73px;
    background: linear-gradient(180deg, var(--seal) 0%, var(--seal-dark) 100%);
  }
  .pack__swoosh { position: absolute; left: 0; top: 0; }
  .pack__logo {
    position: absolute; left: 141px; top: 121px; width: 263px; height: 72px;
    background: var(--label);
    display: flex; align-items: center; justify-content: center;
    font-size: 20px; letter-spacing: 0.3px;
  }
  .pack__title {
    position: absolute; left: 0; right: 0; top: 270px;
    text-align: center; white-space: nowrap;
    font-family: "Fjalla One", sans-serif;
    font-size: 58px; line-height: 66px; letter-spacing: -0.5px;
    text-transform: uppercase;
  }
  .pack__subtitle {
    position: absolute; left: 25px; top: 422px; width: 488px; height: 36px;
    background: var(--band);
    display: flex; align-items: center; justify-content: center;
    font-size: 21px;
  }
  .pack__visual {
    position: absolute; left: -20px; top: 540px; width: 420px; height: 580px;
    border-radius: 45% 55% 40% 60% / 40% 45% 55% 60%;
    background: radial-gradient(ellipse at 45% 40%, var(--splash-b) 0%, #e3a85c 40%, var(--splash-a) 75%, rgba(199,118,44,0) 100%);
  }
  .pack__claims {
    position: absolute; left: 330px; top: 588px; width: 200px; height: 170px;
  }
  .pack__claims svg { position: absolute; inset: 0; }
  .pack__claims ul {
    position: absolute; left: 34px; top: 42px; list-style: none;
    font-size: 20px; line-height: 28px;
  }
  .pack__claims li::before {
    content: ""; display: inline-block; width: 10px; height: 10px;
    border-radius: 50%; background: var(--ink); margin-right: 12px;
    vertical-align: 2px;
  }
  .pack__weight {
    position: absolute; right: 44px; top: 1012px;
    font-family: "Fjalla One", sans-serif; font-size: 34px;
  }
</style>
</head>
<body>
  <div class="pack">
    <svg class="pack__swoosh" width="520" height="1110" viewBox="0 0 520 1110" aria-hidden="true">
      <path d="M0 490 C 140 520 250 640 300 760 C 340 860 420 980 520 1000 L520 1110 L0 1110 Z" fill="var(--bag-light)" opacity="0.6"/>
    </svg>
    <div class="pack__seal"></div>
    <div class="pack__logo">LOGO PLATZHALTER</div>
    <h1 class="pack__title">Erdnuss-Karamell<br>Bites</h1>
    <p class="pack__subtitle">Erdnusswürfel ummantelt in Karamell</p>
    <div class="pack__visual" role="img" aria-label="Erdnuss mit Karamellspritzern und Erdnussstückchen"></div>
    <div class="pack__claims">
      <svg width="200" height="170" viewBox="0 0 200 170" aria-hidden="true">
        <path d="M95 6 C 40 4 8 40 8 88 C 8 140 60 166 110 160 C 165 154 196 118 192 74 C 189 40 165 16 128 8" fill="none" stroke="var(--ink)" stroke-width="3.5" stroke-linecap="round"/>
      </svg>
      <ul>
        <li>vegan</li>
        <li>proteinreich</li>
        <li>glutenfrei</li>
      </ul>
    </div>
    <div class="pack__weight">XX G</div>
  </div>
</body>
</html>
```